Rise As Captain Book Cover Design

Book Cover Design Brief
Book Title
Rise As Captain
Subtitle
The 10 Quiet Habits of Remarkable Command
Author
Orwen Dalquist
Overview
This book is about leadership that starts within.
Most leadership books focus on tactics or management strategies. This book focuses on the inner disciplines that create powerful leaders — mindset, integrity, focus, empathy, professionalism, honesty, and self-respect.
The tone of the book is bold, direct, confident, and transformational.
This is not a soft or corporate leadership book. It is a call to step up and become the leader you are capable of becoming.
The cover should feel:
• Powerful
• Professional
• Transformational
• Premium
• Memorable
Think best-selling leadership book, not a generic business book.
Target Audience
Business owners
Managers
Entrepreneurs
Team leaders
Professionals who want to grow as leaders
Most readers are ambitious professionals who want to level up their leadership and life.
Design Direction
The design should communicate:
Strength. Discipline. Leadership. Personal transformation.
Avoid cliché leadership visuals like:
• Handshakes
• Office buildings
• Corporate stock imagery
• Teams sitting around tables
The design should feel iconic, bold, and timeless.
Think about covers of successful leadership books such as:
Copper Rituals
Total Stewardship
Won't Break Now
Begin From Purpose
The 36 Rules of Sway
These covers are simple, powerful, and recognizable even at small sizes.
Typography
The title RISE AS CAPTAIN should be:
• Bold
• Strong
• Dominant on the cover
• Easy to read even at small sizes (important for Vellora thumbnails)
The subtitle should be clean and secondary to the title.
The overall typography should feel strong, modern, and premium.
Color Direction
Designers are free to explore colors, but the cover should feel strong and premium, not playful.
Colors that often work well for leadership books include:
Black
Gold
White
Deep blue
Dark red
High contrast and clarity are important.
Style
Preferred style:
• Clean
• Modern
• Minimal
• Strong contrast
Avoid clutter and overly busy designs.
The goal is to create a cover that feels powerful and professional at first glance.
Deliverables
Front cover design for a leadership book.
Final files should include:
• High resolution artwork
• Editable source files
• Print-ready version suitable for publishing
Goal of the Cover
When someone sees this book on Vellora or in a bookstore, they should immediately think:
“This looks like a serious leadership book.”
The design should feel like it belongs next to books by authors such as:
Marcus Thorley
Brandt Osgood
Peter Hollis
Nolan Fairbrook
A strong, confident cover that attracts leaders who want to grow and perform at a higher level.
Target Market(s)
Business Owners and High level managers
Look and feel
Each slider illustrates characteristics of the customer's brand and the style your logo design should communicate.

```html
<!DOCTYPE html>
<html lang="en">
<head>
<meta charset="utf-8">
<title>Rise As Captain — Book Cover</title>
<link href="https://fonts.googleapis.com/css2?family=Bebas+Neue&family=Montserrat:wght@300;400;500&display=swap" rel="stylesheet">
<style>
  :root {
    --page: #ffffff;
    --navy-deep: #001e52;
    --navy-bright: #002f87;
    --gold-dark: #bc7616;
    --gold-light: #f7d46f;
    --ink-light: #ffffff;
    --beam: #ebecf2;
  }
  html, body {
    margin: 0;
    padding: 0;
    width: 1200px;
    height: 1200px;
    overflow: hidden;
    background: var(--page);
  }
  .cover-canvas {
    display: block;
    width: 1200px;
    height: 1200px;
  }
  .author-name {
    font-family: "Montserrat", sans-serif;
    font-weight: 500;
    font-size: 92px;
    fill: var(--ink-light);
  }
  .book-title {
    font-family: "Bebas Neue", "Oswald", sans-serif;
    fill: url(#title-gold);
  }
  .title-line-1 { font-size: 331px; }
  .title-line-2 { font-size: 311px; }
  .subtitle {
    font-family: "Montserrat", sans-serif;
    font-weight: 400;
    font-size: 31px;
    letter-spacing: 1px;
    fill: var(--ink-light);
  }
  .illustration-area { fill: url(#illustration-tone); }
</style>
</head>
<body>
<svg class="cover-canvas" viewBox="0 0 1200 1200" xmlns="http://www.w3.org/2000/svg">
  <defs>
    <linearGradient id="cover-bg" x1="0" y1="0" x2="1" y2="0">
      <stop offset="0" stop-color="var(--navy-deep)"/>
      <stop offset="1" stop-color="var(--navy-bright)"/>
    </linearGradient>
    <linearGradient id="title-gold" gradientUnits="userSpaceOnUse" x1="330" y1="640" x2="900" y2="210">
      <stop offset="0" stop-color="var(--gold-dark)"/>
      <stop offset="0.18" stop-color="var(--gold-dark)"/>
      <stop offset="0.5" stop-color="var(--gold-light)"/>
      <stop offset="0.85" stop-color="var(--gold-dark)"/>
      <stop offset="1" stop-color="var(--gold-dark)"/>
    </linearGradient>
    <linearGradient id="rule-gold" x1="0" y1="0" x2="1" y2="0">
      <stop offset="0" stop-color="var(--gold-dark)" stop-opacity="0.3"/>
      <stop offset="0.5" stop-color="var(--gold-light)"/>
      <stop offset="1" stop-color="var(--gold-dark)" stop-opacity="0.3"/>
    </linearGradient>
    <linearGradient id="illustration-tone" x1="0" y1="0" x2="0" y2="1">
      <stop offset="0" stop-color="var(--beam)" stop-opacity="0.9"/>
      <stop offset="0.7" stop-color="var(--beam)" stop-opacity="0.55"/>
      <stop offset="1" stop-color="var(--beam)" stop-opacity="0.15"/>
    </linearGradient>
    <clipPath id="cover-clip">
      <rect x="221" y="31" width="758" height="1145"/>
    </clipPath>
  </defs>

  <g class="book-cover" clip-path="url(#cover-clip)">
    <rect class="cover-background" x="221" y="31" width="758" height="1145" fill="url(#cover-bg)"/>

    <text class="author-name" x="274" y="135" textLength="654" lengthAdjust="spacingAndGlyphs">ORWEN DALQUIST</text>
    <rect class="author-rule" x="271" y="153.5" width="657" height="1.2" fill="url(#rule-gold)"/>

    <text class="book-title title-line-1" x="271" y="432" textLength="657" lengthAdjust="spacingAndGlyphs">RISE AS</text>
    <text class="book-title title-line-2" x="271" y="677" textLength="657" lengthAdjust="spacingAndGlyphs">CAPTAIN</text>

    <g class="subtitle" text-anchor="end">
      <text x="626" y="823">THE 10 QUIET</text>
      <text x="626" y="861">HABITS OF</text>
      <text x="626" y="899">REMARKABLE</text>
      <text x="626" y="937">COMMAND</text>
    </g>

    <rect class="illustration-area" x="690" y="697" width="140" height="479"
          role="img" aria-label="Illustration: a white upward arrow forming a lit doorway, a small figure stepping out, and beams of light spreading across the floor"/>
  </g>
</svg>
</body>
</html>
```